Alapca breeding needs a website

Presentation of the farm, animals (stallions, mares, information about the animals, for sale) and possible later expansion with a webshop (alpaca wool products). We want to present our farm and the animals on the farm on this page. A mission why we are doing this. Furthermore, each animal should be shown with a picture and described. Later we want to sell our own products made from alpaca wool via a webshop. But we still need to grow a bit to do that.

Target Market(s)

Information about my alpaca breeding and the alpaca farm

Industry/Entity Type

Tierzucht

Number of Pages Required

1 page

Font styles to use
Sans Serif

Requirements
Must have
• Modern design that matches the logo
Nice to have
• Intuitive operation / Clear structure
Should not have
• No

```html
<!DOCTYPE html>
<html lang="en">
<head>
<meta charset="utf-8">
<title>Meadowvale Alpacas</title>
<link rel="stylesheet" href="https://fonts.googleapis.com/css2?family=Cinzel:wght@400;700;900&family=Roboto:wght@400;500&display=swap">
<style>
:root{
  --navy:#0f2a44;
  --green:#7dc142;
  --green-dark:#3f7a1c;
  --text:#555c63;
  --rule:#c9cdd1;
  --white:#ffffff;
}
*{margin:0;padding:0;box-sizing:border-box}
html,body{width:1200px;height:3648px;overflow:hidden;background:var(--white)}
body{position:relative;font-family:'Roboto',sans-serif;color:var(--text)}
.abs{position:absolute}
.cinzel{font-family:'Cinzel',serif}
.brand{font-family:'Cinzel',serif;font-weight:700;color:var(--navy);display:flex;align-items:center;gap:12px}
.brand .dot{width:26px;height:26px;border-radius:50%;background:var(--green)}
.topinfo{font-family:'Cinzel',serif;font-weight:700;font-size:14px;color:var(--navy);line-height:21px;display:flex;gap:12px;align-items:center}
.nav{display:flex;gap:36px;font-family:'Cinzel',serif;font-weight:700;font-size:15px;color:var(--navy)}
.nav .active{color:var(--green)}
.btn{position:absolute;width:160px;height:44px;border-radius:22px;background:var(--green);box-shadow:0 4px 0 var(--green-dark);color:#163a10;font-weight:500;font-size:15px;display:flex;align-items:center;justify-content:center;gap:30px}
.photo{position:absolute}
.eyebrow{font-family:'Cinzel',serif;font-weight:700;font-size:19px;color:var(--navy)}
.title{font-family:'Cinzel',serif;font-weight:700;font-size:42px;color:var(--navy)}
.para{font-size:15.5px;line-height:24px;color:var(--text)}
.circle{position:absolute;border-radius:50%}
.feature{position:absolute;width:220px;text-align:center}
.feature .ring{width:140px;height:140px;margin:0 auto;border-radius:50%;border:6px solid var(--navy);border-top-color:transparent;display:flex;align-items:center;justify-content:center}
.feature .label{margin-top:18px;font-family:'Cinzel',serif;font-weight:700;font-size:18px;color:var(--navy)}
.foot-h{font-family:'Cinzel',serif;font-size:22px;color:var(--navy)}
.foot-t{font-size:15px;color:#333;line-height:22px}
.links a{display:block;font-size:13.5px;color:#333;text-decoration:none;margin-bottom:15px}
</style>
</head>
<body>

<!-- Header -->
<div class="abs brand" style="left:110px;top:95px;font-size:28px"><span class="dot"></span>Meadowvale</div>
<div class="abs topinfo" style="left:688px;top:18px">
  <svg width="36" height="36" viewBox="0 0 24 24" fill="none" stroke="#7dc142" stroke-width="1.6"><path d="M12 21s-6-6.2-6-11a6 6 0 0 1 12 0c0 4.8-6 11-6 11z"/><circle cx="12" cy="10" r="2.3"/><path d="M5 21h14"/></svg>
  <div>42 Orchard Lane<br>Fernbrook, NJ 08045</div>
</div>
<div class="abs" style="left:912px;top:20px;width:1px;height:38px;background:var(--navy)"></div>
<div class="abs topinfo" style="left:938px;top:18px">
  <svg width="36" height="36" viewBox="0 0 24 24" fill="none" stroke="#7dc142" stroke-width="1.6"><path d="M5 3h4l2 5-2.5 1.5a11 11 0 0 0 6 6L16 13l5 2v4a2 2 0 0 1-2 2A16 16 0 0 1 3 5a2 2 0 0 1 2-2z"/></svg>
  <div>Call Us<br>+10 555 0142</div>
</div>
<div class="abs" style="left:323px;top:80px;width:765px;height:1px;background:var(--navy)"></div>
<nav class="abs nav" style="left:434px;top:110px">
  <span class="active">Home</span><span>About Us</span><span>What We Offer</span><span>Products</span><span>Blog</span><span>Contact Us</span>
</nav>

<!-- Hero -->
<div class="photo" role="img" aria-label="Alpaca standing by a mountain lake with snowy peaks" style="left:0;top:165px;width:1200px;height:600px;background:linear-gradient(180deg,#4f7fa8 0%,#9bb8cf 35%,#5d84a0 55%,#b08a48 75%,#f2f2f2 100%);border-radius:0 0 40% 30% / 0 0 30px 20px"></div>
<div class="abs cinzel" style="left:112px;top:340px;font-size:40px;color:#fff">Welcome To</div>
<div class="abs cinzel" style="left:110px;top:380px;font-size:78px;font-weight:900;color:var(--green);line-height:72px">Meadowvale<br>Alpacas</div>
<div class="btn" style="left:112px;top:543px">Read More <span>&gt;</span></div>
<div class="circle" style="left:34px;top:440px;width:44px;height:44px;background:#fff;display:flex;align-items:center;justify-content:center;font-weight:700;font-size:22px;color:var(--navy)">&lt;</div>
<div class="circle" style="left:1122px;top:440px;width:44px;height:44px;background:#fff;display:flex;align-items:center;justify-content:center;font-weight:700;font-size:22px;color:var(--green)">&gt;</div>

<!-- Our Story -->
<div class="abs brand" style="left:110px;top:770px;font-size:20px"><span class="dot" style="width:60px;height:60px;background:var(--navy)"></span></div>
<div class="abs eyebrow" style="left:112px;top:862px">Our Story</div>
<div class="abs title" style="left:112px;top:888px">Meadowvale Alpacas</div>
<div class="abs" style="left:112px;top:943px;width:56px;height:2px;background:var(--green)"></div>
<p class="abs para" style="left:112px;top:968px;width:452px">Lorem ipsum dolor sit amet, consectetur adipiscing elit, sed do eiusmod tempor incididunt ut labore et dolore magna aliqua. Ut enim ad minim veniam, quis nostrud exercitation ullamco laboris nisi ut aliquip ex ea commodo consequat.</p>
<p class="abs para" style="left:112px;top:1088px;width:452px">Duis aute irure dolor in reprehenderit in voluptate velit esse cillum dolore eu fugiat nulla pariatur. Excepteur sint occaecat cupidatat non proident, sunt in culpa qui officia deserunt mollit anim id est</p>
<div class="btn" style="left:112px;top:1179px">Read More <span>&gt;</span></div>

<svg class="abs" style="left:680px;top:905px" width="320" height="120" viewBox="0 0 320 120" fill="none" stroke="#7dc142" stroke-width="3">
  <path d="M62 4H8v100"/><path d="M0 96l8 12 8-12z" fill="#7dc142"/>
  <path d="M258 4h26v100"/><path d="M276 96l8 12 8-12z" fill="#7dc142"/>
</svg>
<div class="circle" role="img" aria-label="Herd of alpacas grazing in a mountain valley" style="left:743px;top:818px;width:184px;height:184px;background:linear-gradient(180deg,#8a8f94,#7a6a4a 55%,#c9b890)"></div>
<div class="circle" role="img" aria-label="Alpaca beside shelves of colourful wool yarn" style="left:600px;top:1020px;width:184px;height:184px;background:radial-gradient(circle at 40% 60%,#d63a6a,#8a4a2a 60%,#5a3a2a)"></div>
<div class="circle" role="img" aria-label="Stack of soft alpaca wool knitwear" style="left:904px;top:1020px;width:184px;height:184px;background:radial-gradient(circle,#f3e6d2,#d8bf9c)"></div>
<div class="photo" role="img" aria-label="Sketch of an alpaca wearing a flower crown" style="left:795px;top:1198px;width:125px;height:167px;background:linear-gradient(180deg,#f4f4f4,#e2e2e2)"></div>

<!-- Video band -->
<div class="photo" role="img" aria-label="Group of alpacas in a row in a green meadow" style="left:0;top:1365px;width:1200px;height:467px;background:linear-gradient(180deg,#34402c 0%,#5a4a3a 40%,#8a6e58 70%,#4a3c30 100%)"></div>
<div class="abs cinzel" style="left:0;top:1482px;width:1200px;text-align:center;font-size:50px;font-weight:900;color:var(--green);line-height:72px">Growing a Stronger<br>Tomorrow</div>
<div class="circle" style="left:567px;top:1634px;width:66px;height:66px;background:#fff"></div>
<svg class="abs" style="left:590px;top:1652px" width="26" height="30" viewBox="0 0 26 30"><path d="M2 2l22 13L2 28z" fill="#7dc142"/></svg>

<!-- Farm Story -->
<div class="photo" role="img" aria-label="Illustrated alpaca wearing glasses" style="left:1045px;top:1862px;width:125px;height:155px;background:linear-gradient(180deg,#efe6da,#d9c6ad)"></div>
<div class="photo" role="img" aria-label="Illustrated standing alpaca" style="left:38px;top:2145px;width:82px;height:140px;background:linear-gradient(180deg,#f2ede4,#ddd0bd)"></div>
<div class="circle" style="left:548px;top:1905px;width:104px;height:104px;background:var(--navy)"></div>
<div class="abs eyebrow" style="left:0;top:2020px;width:1200px;text-align:center">Our Farm Story</div>
<div class="abs title" style="left:0;top:2045px;width:1200px;text-align:center">The Alpaca Farm</div>
<div class="abs" style="left:572px;top:2100px;width:56px;height:2px;background:var(--green)"></div>
<p class="abs para" style="left:235px;top:2124px;width:730px;text-align:center">Lorem ipsum dolor sit amet, consectetur adipiscing elit, sed do eiusmod tempor incididunt ut labore et dolore magna aliqua. Ut enim ad minim veniam, quis nostrud exercitation ullamco laboris nisi ut aliquip ex ea commodo consequat.</p>
<p class="abs para" style="left:235px;top:2220px;width:730px;text-align:center">Duis aute irure dolor in reprehenderit in voluptate velit esse cillum dolore eu fugiat nulla pariatur. Excepteur sint occaecat cupidatat non proident, sunt in culpa qui officia deserunt mollit anim id est laborum.</p>

<div class="feature" style="left:108px;top:2310px"><div class="ring"><svg width="60" height="56" viewBox="0 0 60 56" fill="none" stroke="#0f2a44" stroke-width="4"><path d="M6 24L30 6l24 18v28H6z"/><path d="M22 52V34h16v18M22 34l16 18M38 34L22 52"/></svg></div><div class="label">Modern Farm</div></div>
<div class="feature" style="left:363px;top:2310px"><div class="ring"><svg width="60" height="56" viewBox="0 0 60 56" fill="none" stroke="#0f2a44" stroke-width="4"><path d="M18 50c0-22 12-36 36-40-2 24-16 36-36 40z"/><path d="M18 50c4-14 14-24 24-30"/></svg></div><div class="label">Natural &amp; Organic</div></div>
<div class="feature" style="left:617px;top:2310px"><div class="ring"><svg width="60" height="56" viewBox="0 0 60 56" fill="none" stroke="#0f2a44" stroke-width="4"><circle cx="28" cy="28" r="22"/><path d="M12 16c14 2 26 14 30 30M8 28c12 0 22 8 26 20M20 8c12 6 22 18 26 30"/><path d="M48 48h10"/></svg></div><div class="label">Best Products</div></div>
<div class="feature" style="left:872px;top:2310px"><div class="ring"><svg width="60" height="60" viewBox="0 0 60 60" fill="none" stroke="#0f2a44" stroke-width="4"><circle cx="30" cy="24" r="18"/><path d="M30 14l3 7h7l-6 4 2 7-6-4-6 4 2-7-6-4h7z"/><path d="M20 40l-4 16 8-5 6 6M40 40l4 16-8-5-6 6"/></svg></div><div class="label">Awarded Farm</div></div>

<div class="btn" style="left:520px;top:2566px">Read More <span>&gt;</span></div>

<!-- Landscape -->
<div class="photo" role="img" aria-label="Two llamas standing on a green mountainside" style="left:0;top:2650px;width:1200px;height:430px;background:linear-gradient(180deg,#e8eef0 0%,#9fb8a8 25%,#4f7a4a 55%,#8a8a3a 80%,#5a5a2a 100%)"></div>

<!-- Newsletter -->
<div class="abs brand" style="left:270px;top:3235px;font-size:36px"><span class="dot"></span>Meadowvale</div>
<div class="abs cinzel" style="left:520px;top:3163px;font-size:21px;font-weight:700;color:var(--green)">Sign Up Our Newsletter</div>
<div class="abs" style="left:520px;top:3207px;width:408px;height:38px;border:1.5px solid #7a8088;border-radius:19px;display:flex;align-items:center;justify-content:space-between;padding:0 16px;font-size:14px;color:#555">EMAIL
  <svg width="22" height="14" viewBox="0 0 22 14" fill="none" stroke="#333" stroke-width="1.5"><path d="M1 13L20 3M12 1l8 2-3 7"/></svg></div>

<!-- Footer -->
<div class="abs" style="left:0;top:3340px;width:1200px;height:1px;background:var(--rule)"></div>
<div class="abs foot-h" style="left:115px;top:3370px">Contact Us</div>
<div class="abs foot-t" style="left:112px;top:3412px;display:flex;gap:16px"><svg width="12" height="16" viewBox="0 0 12 16"><path d="M6 16S0 9 0 6a6 6 0 0 1 12 0c0 3-6 10-6 10z" fill="#7dc142"/></svg><div>Brookfield Road, Elm Hollow,<br>Co. Larch, H21 K407</div></div>
<div class="abs foot-t" style="left:112px;top:3473px;display:flex;gap:16px"><svg width="14" height="14" viewBox="0 0 24 24"><path d="M5 3h4l2 5-2.5 1.5a11 11 0 0 0 6 6L16 13l5 2v4a2 2 0 0 1-2 2A16 16 0 0 1 3 5a2 2 0 0 1 2-2z" fill="#7dc142"/></svg>+10 555 0142</div>
<div class="abs foot-t" style="left:112px;top:3514px;display:flex;gap:16px"><svg width="14" height="14" viewBox="0 0 14 14"><rect x="1" y="3" width="12" height="9" fill="none" stroke="#7dc142" stroke-width="2"/><path d="M1 3l6 5 6-5" fill="none" stroke="#7dc142" stroke-width="1.5"/></svg>hello@meadowvale-farm.test</div>
<div class="abs" style="left:454px;top:3378px;width:1px;height:162px;background:var(--rule)"></div>
<div class="abs foot-h" style="left:525px;top:3370px">Quick Links</div>
<div class="abs links" style="left:525px;top:3414px"><a>Home</a><a>About Us</a><a>What We Offer</a></div>
<div class="abs links" style="left:685px;top:3414px"><a>Products</a><a>Blog</a><a>Contact Us</a></div>
<div class="abs" style="left:805px;top:3378px;width:1px;height:162px;background:var(--rule)"></div>
<div class="abs foot-h" style="left:948px;top:3368px">Follow Us</div>
<div class="abs" style="left:948px;top:3408px;display:flex;gap:14px;align-items:center">
  <span class="circle" style="position:static;display:block;width:44px;height:44px;background:var(--green)"></span>
  <span class="circle" style="position:static;display:block;width:18px;height:18px;border:2px solid #9aa3ad"></span>
  <span class="circle" style="position:static;display:block;width:18px;height:18px;border:2px solid #9aa3ad"></span>
  <span class="circle" style="position:static;display:block;width:18px;height:18px;border:2px solid #9aa3ad"></span>
</div>
<div class="abs" style="left:0;top:3583px;width:1200px;height:1px;background:var(--rule)"></div>
<div class="abs" style="left:0;top:3606px;width:1200px;text-align:center;font-size:14.5px;color:#333">Copyright © 2024 Meadowvale Alpacas – All rights reserved.</div>

</body>
</html>
```